依頼詳細
ポスティング形式での営業となりますので、
一目見て目に付くようなチラシデザインで
あれば、多少デザインに派手さが入っても
良いとは思っています。

「本当に和室のままでイイですか?」
というアラートの様なタイトルがどれだけ
目を引くかに重点を置いて考えています。

また、何故和室を洋室に変えた方がイイと
いう根拠につきましては、
・畳の経年寿命の早さとメンテナンス&交換をしてない畳のアレルギー等の促進を
進めるという情報をわかりやすくアラートをお伝えした文章が欲しいです。(ハウスダスト・ダニ・花粉)

価格帯の記載
・マンションアパートタイプであれば
1畳単価50000円〜
・戸建てタイプの場合い1畳単価60000円〜
押し入れのクローゼット化 10000円〜

室内の物の移動等も含める作業は別途
お見積もりとの別記載も入れて欲しい。

和室〜洋室に変えた際のビフォーアフターの
写真等も添付したいです。
記載項目
翠昇株式会社 03-6812-3097
HP https://suishoweb.ne.jp/
キャッチコピー「和室のままで本当にイイですか?」
サイズ
A4
ページ数
両面
希望イメージ
シンプル 複雑
単色 カラフル
暗い 明るい
日常 高級
遊び心 厳粛
未来的 伝統的
女性的 男性的
希望する色
青系
納品ファイル
• 高解像度JPG (.jpg)
• PNG形式 (.png)
補足説明
デザイン 文章 画像についても提案があれば都度頂きたい。
■ 選んだ理由

シンプルで有りながらも、ディテールの部分の丁寧さがスゴく見やすく思えました。文章につきましても
拙い説明にも関わらず、しっかり拾い上げて頂けたのが1番決め手となりました。本当にありがとうございます。

■ 提案者全員のお礼・コメント

この度は沢山のご提案頂きありがとうございました。
タスクフォルンを使ったのは初めてで、色々分からず皆様に失礼が有りましたらここでお詫びさせて下さい。

とてもタスクフォルンのサービスとデザイナーの皆様の
技術に大変関心を持ちました。今後も色んな事で
運用したいと思っておりますので、また機会が
ございましたら何卒よろしくお願い致します。

この度は誠に有難うございました。

```html
<!DOCTYPE html>
<html lang="ja">
<head>
<meta charset="utf-8">
<title>本当に和室のままでイイですか？</title>
<link href="https://fonts.googleapis.com/css2?family=M+PLUS+1p:wght@500;700;800&display=swap" rel="stylesheet">
<style>
  :root{
    --paper:#f6f1e1;
    --ink:#2e2a28;
    --purple:#8a3a8a;
    --blue:#2f7fc3;
    --tatami:#c9c48a;
    --tatami-dark:#a9a66a;
    --wall:#efe6cf;
  }
  html,body{margin:0;padding:0;overflow:hidden;background:var(--paper);}
  .flyer{
    position:relative;width:849px;height:1200px;overflow:hidden;
    background:var(--paper);color:var(--ink);
    font-family:"M PLUS 1p",sans-serif;
  }
  .company{position:absolute;right:40px;top:34px;text-align:left;}
  .company-name{font-size:30px;font-weight:800;letter-spacing:1px;margin:0;}
  .company-tel{display:flex;align-items:center;gap:6px;font-size:16px;font-weight:700;margin:4px 0 0;}
  .company-url{font-size:14px;font-weight:500;margin:2px 0 0;}
  .headline{
    position:absolute;left:40px;top:78px;margin:0;
    display:flex;flex-direction:row;gap:14px;
    font-size:128px;font-weight:800;line-height:1;
  }
  .headline span{writing-mode:vertical-rl;text-orientation:upright;letter-spacing:-4px;}
  .headline .accent{color:var(--purple);}
  .headline .late{margin-top:26px;}
  .room-illustration{position:absolute;left:430px;top:190px;width:400px;height:390px;}
  .care-bubble{
    position:absolute;right:28px;top:196px;width:120px;
    font-size:19px;font-weight:700;line-height:1.2;text-align:center;
    transform:rotate(-14deg);
  }
  .risk-text{
    position:absolute;right:26px;top:612px;margin:0;
    writing-mode:vertical-rl;
    font-size:33px;font-weight:700;line-height:1.12;height:420px;letter-spacing:1px;
  }
  .risk-text em{font-style:normal;color:var(--blue);}
  .offer{position:absolute;left:90px;top:1040px;}
  .offer-lead{
    display:inline-block;font-size:26px;font-weight:700;
    border:2.5px solid var(--ink);border-radius:26px;padding:4px 22px;
  }
  .offer-main{margin:14px 0 0 28px;font-size:58px;font-weight:800;letter-spacing:1px;}
  .offer-main .accent{color:var(--blue);}
  .chair-illustration{position:absolute;left:730px;top:1070px;width:70px;height:100px;}
</style>
</head>
<body>
<div class="flyer">
  <div class="company">
    <p class="company-name">翠昇株式会社</p>
    <p class="company-tel">
      <svg width="16" height="16" viewBox="0 0 16 16" aria-hidden="true"><rect x="1" y="1" width="14" height="14" rx="2" fill="none" stroke="currentColor" stroke-width="1.6"/><path d="M5 4c0 4 3 8 7 8l0-2-2-1-1 1c-1-1-2-2-3-3l1-1-1-2z" fill="currentColor"/></svg>
      03-6812-3097
    </p>
    <p class="company-url">https://suishoweb.ne.jp/</p>
  </div>

  <h1 class="headline">
    <span>本当に</span>
    <span class="accent">和室のままで</span>
    <span class="late">イイですか？</span>
  </h1>

  <svg class="room-illustration" viewBox="0 0 400 390" role="img" aria-label="畳の和室で掛け軸を眺めて困った様子の男性のイラスト">
    <defs>
      <linearGradient id="roomTone" x1="0" y1="0" x2="0" y2="1">
        <stop offset="0" stop-color="var(--wall)"/>
        <stop offset="0.45" stop-color="var(--tatami)"/>
        <stop offset="1" stop-color="var(--tatami-dark)"/>
      </linearGradient>
    </defs>
    <rect x="0" y="0" width="400" height="390" rx="8" fill="url(#roomTone)"/>
  </svg>
  <p class="care-bubble">畳のお手入れしてますか？</p>

  <p class="risk-text">畳は経年寿命が早く定期的にメンテナンスや交換をしないと、<em>ハウスダスト・ダニ・花粉アレルギー</em>などを引き起こす可能性が高くなります。</p>

  <div class="offer">
    <span class="offer-lead">お手入れがラクな</span>
    <p class="offer-main"><span class="accent">洋室</span>にしませんか？</p>
  </div>

  <svg class="chair-illustration" viewBox="0 0 70 100" role="img" aria-label="青い椅子のイラスト">
    <rect x="0" y="0" width="70" height="100" rx="6" fill="var(--blue)"/>
  </svg>
</div>
</body>
</html>
```